Vesk in Spain

web design of search platform. Enclosed please find an excel sheet with the info, as well as a picture of a webdesign we like (plumhollow). Idea is to have a modern, inviting website with main colors white, red and dark grey (text). The logo (pold) will be changed to vesk, but you can use this logo for now. Please also use the character enclosed. We can ask this designer to also design the pictograms for the other items, just use something from the net for the design and we'll have it changed afterwards. The texts are enclosed in the word doc enclosed. Thank you!

Target Market(s)

people looking for property in Spain

Industry/Entity Type

Real Estate

Number of Pages Required

1 page

Other font styles liked:
• a font that goes well with the logo

Colors
ec1f27

Requirements
Must have
• a lot of white
• clean but fun look

```html
<!DOCTYPE html>
<html lang="en">
<head>
<meta charset="utf-8">
<title>Vesk</title>
<link href="https://fonts.googleapis.com/css2?family=Quicksand:wght@400;500;700&display=swap" rel="stylesheet">
<style>
  :root {
    --red: #ec1f27;
    --dark: #231f20;
    --panel: #262324;
    --white: #ffffff;
    --grey-text: #9a9a9a;
    --field: #f3f3f3;
    --text: #3a3a3a;
  }
  * { box-sizing: border-box; margin: 0; padding: 0; }
  html, body { width: 1200px; height: 752px; overflow: hidden; background: var(--white); }
  body { font-family: "Quicksand", sans-serif; color: var(--text); position: relative; }

  .site-header { position: absolute; left: 0; top: 0; width: 1200px; height: 86px; }
  .brand {
    position: absolute; left: 118px; top: 28px;
    font-size: 24px; font-weight: 500; color: var(--dark); letter-spacing: 0.01em;
    display: flex; align-items: center; gap: 7px;
  }
  .brand-dot { width: 8px; height: 8px; border-radius: 50%; background: var(--red); }
  .menu-toggle { position: absolute; left: 1050px; top: 36px; width: 30px; height: 14px; }
  .menu-toggle span { position: absolute; right: 0; height: 3px; }
  .menu-toggle .bar-top { top: 0; width: 30px; background: var(--dark); }
  .menu-toggle .bar-bottom { top: 11px; width: 22px; background: var(--red); }

  .hero { position: absolute; left: 0; top: 86px; width: 1200px; height: 436px; }
  .hero-intro {
    position: absolute; left: 0; top: 0; width: 478px; height: 436px;
    background: var(--red); color: var(--white); text-align: center;
  }
  .hero-title { position: absolute; left: 0; width: 478px; top: 112px; font-weight: 400; font-size: 21px; line-height: 30px; }
  .hero-title strong { display: block; font-weight: 700; font-size: 22px; letter-spacing: 0.12em; text-transform: uppercase; }
  .hero-lead { position: absolute; left: 84px; width: 312px; top: 212px; font-size: 14.6px; line-height: 25.6px; font-weight: 500; }

  .hero-search { position: absolute; left: 478px; top: 0; width: 722px; height: 436px; background: var(--panel); }
  .search-label { position: absolute; left: 122px; top: 178px; font-size: 11.5px; color: var(--grey-text); }
  .search-form { position: absolute; left: 122px; top: 206px; width: 478px; height: 48px; display: flex; }
  .search-field { flex: 1; background: var(--field); display: flex; align-items: center; padding-left: 13px; }
  .search-button {
    width: 136px; background: var(--red); color: var(--white); border: 0;
    font-family: "Quicksand", sans-serif; font-size: 12px; font-weight: 500; letter-spacing: 0.02em;
  }

  .dot { position: absolute; border-radius: 50%; background: var(--dark); }
  .dot-large { left: 32px; top: 503px; width: 70px; height: 70px; }
  .dot-small { left: 99px; top: 490px; width: 26px; height: 26px; }

  .promise { position: absolute; left: 0; top: 610px; width: 1200px; text-align: center; }
  .promise-kicker { font-size: 15px; letter-spacing: 0.04em; color: var(--text); }
  .promise-line { margin-top: 8px; font-size: 24px; font-weight: 400; letter-spacing: 0.33em; color: var(--dark); }
  .promise-line .initial { color: var(--red); font-size: 34px; letter-spacing: 0.24em; }
</style>
</head>
<body>
  <header class="site-header">
    <div class="brand"><span>pold</span><span class="brand-dot"></span></div>
    <div class="menu-toggle" aria-label="Menu"><span class="bar-top"></span><span class="bar-bottom"></span></div>
  </header>

  <section class="hero">
    <div class="hero-intro">
      <h1 class="hero-title">Estate Agents Compete,<strong>You Win!</strong></h1>
      <p class="hero-lead">Stay anonymous while the estate agents of your choice compete for you by sending you their best proposal, thus guaranteeing you the best deal possible.</p>
    </div>
    <div class="hero-search">
      <p class="search-label">Enter the city or area whre you want to buy or sell</p>
      <div class="search-form">
        <div class="search-field">
          <svg width="22" height="28" viewBox="0 0 22 28" aria-hidden="true">
            <path d="M11 26 C11 26 2 16 2 10 A9 9 0 0 1 20 10 C20 16 11 26 11 26 Z" fill="none" stroke="#8a8a8a" stroke-width="1.6"/>
            <circle cx="11" cy="10" r="3" fill="none" stroke="#8a8a8a" stroke-width="1.6"/>
          </svg>
        </div>
        <button class="search-button" type="button">COMPARE AGENTS</button>
      </div>
    </div>
  </section>

  <div class="dot dot-large"></div>
  <div class="dot dot-small"></div>

  <section class="promise">
    <p class="promise-kicker">With vesk you will</p>
    <p class="promise-line"><span class="initial">f</span>ind the <span class="initial">b</span>est real <span class="initial">e</span>state agent for <span class="initial">y</span>ou!</p>
  </section>
</body>
</html>
```